Banners for a bowtie/tie Fashion shop

I need banners (770x100) for a necktie and bowtie shop (http://www.movelia.dk)

5 BOWTIE BANNERS:

I need the 3 text versions for eatch bowtie banner:

Danmarks største udvalg af butterfly
Køb butterfly. FRI fragt og FRI retur
Butterfly fra 199,- inkl. FRI fragt

5 NECKTIE BANNERS:

I need the 3 text versions for eatch necktie banner:

Danmarks største udvalg af slips
Køb slips. FRI fragt og FRI retur
Slips fra 199,- inkl. FRI fragt

All banners should contain the logo. All in JPG format and Photoshop/Inddesign/illustrator format

Target Market(s)

Guys and Gays

Industry/Entity Type

Shop

Requirements
Must have
• Logo
Nice to have
• Nice new pictures

```html
<!DOCTYPE html>
<html lang="da">
<head>
<meta charset="utf-8">
<title>Butterfly banner</title>
<link rel="stylesheet" href="https://fonts.googleapis.com/css2?family=Roboto+Condensed:wght@400;700&display=swap">
<style>
  :root {
    --orange: #f0641e;
    --white: #ffffff;
    --ink: #111111;
    --grey-band: #dedede;
    --box-dark: #161616;
    --box-orange: #d8661c;
    --box-green: #6f8a2c;
    --tie-grey: #8c8f96;
    --tie-plum: #5b4a55;
    --tie-blue: #3aa3d2;
  }
  html, body {
    margin: 0;
    padding: 0;
    width: 1200px;
    height: 156px;
    overflow: hidden;
    background: var(--white);
  }
  .banner {
    position: relative;
    width: 1200px;
    height: 156px;
    display: flex;
    font-family: "Roboto Condensed", "Arial Narrow", sans-serif;
  }
  .gallery {
    display: flex;
    width: 525px;
    height: 156px;
    flex: none;
    background: var(--white);
  }
  .photo { height: 156px; }
  .photo--orange-box {
    width: 176px;
    background:
      radial-gradient(ellipse at 50% 45%, rgba(232,120,40,0.95) 0%, rgba(200,95,25,0.8) 45%, rgba(22,22,22,0.9) 100%),
      var(--box-dark);
  }
  .photo--green-box {
    width: 132px;
    margin-left: 4px;
    background:
      radial-gradient(ellipse at 50% 50%, rgba(130,160,60,0.95) 0%, rgba(90,115,40,0.85) 45%, rgba(22,22,22,0.92) 100%),
      var(--box-dark);
  }
  .photo--grey-tie {
    width: 108px;
    background: linear-gradient(100deg, var(--white) 0%, var(--white) 12%, var(--tie-grey) 30%, var(--tie-plum) 55%, var(--tie-grey) 78%, var(--white) 95%);
  }
  .photo--blue-tie {
    width: 105px;
    background: linear-gradient(100deg, var(--white) 0%, var(--white) 10%, var(--tie-blue) 32%, #6d737c 55%, var(--tie-blue) 75%, var(--white) 95%);
  }
  .messages {
    flex: 1;
    display: flex;
    flex-direction: column;
  }
  .message {
    display: flex;
    align-items: center;
    justify-content: center;
    white-space: nowrap;
    line-height: 1;
  }
  .message--headline {
    height: 52px;
    background: var(--orange);
    color: var(--white);
    font-weight: 700;
    font-size: 40px;
    letter-spacing: -0.2px;
  }
  .message--offer {
    height: 52px;
    background: var(--white);
    color: var(--ink);
    font-size: 38px;
    font-weight: 400;
  }
  .message--offer strong { font-weight: 700; margin-right: 8px; }
  .message--price {
    height: 52px;
    background: linear-gradient(90deg, #d2d2d2 0%, var(--grey-band) 60%, #f2f2f2 100%);
    color: var(--ink);
    font-size: 35px;
    font-weight: 400;
  }
  .message--price strong { font-weight: 700; font-size: 41px; }
</style>
</head>
<body>
  <div class="banner">
    <div class="gallery">
      <div class="photo photo--orange-box" role="img" aria-label="Gaveæske med orange butterflies og slips"></div>
      <div class="photo photo--green-box" role="img" aria-label="Gaveæske med grønne butterflies og slips"></div>
      <div class="photo photo--grey-tie" role="img" aria-label="Ternet gråt slips"></div>
      <div class="photo photo--blue-tie" role="img" aria-label="Stribet blåt slips"></div>
    </div>
    <div class="messages">
      <div class="message message--headline">Danmarks største udvalg af butterfly</div>
      <div class="message message--offer"><strong>Køb butterfly.</strong>FRI fragt og FRI retur</div>
      <div class="message message--price"><strong>Butterfly fra 199,</strong>- inkl. FRI fragt</div>
    </div>
  </div>
</body>
</html>
```